I need the Scorecard I've developed for my staff to be produced into a visually engaging piece that will encourage the staff to utilize it on a daily basis. I'm thinking it could be 5x7 in size so that it isn't too cumbersome, but I'm open to different layouts.
I have multiple other departments that will need Scorecards created for them as well, but each one will contain task specific questions for each department.

```html
<!DOCTYPE html>
<html lang="en">
<head>
<meta charset="utf-8">
<title>Receptionist Daily Excellence Scorecard</title>
<link rel="stylesheet" href="https://fonts.googleapis.com/css2?family=Lato:wght@300;400;700;900&family=Roboto+Condensed:wght@400&family=Poppins:wght@600&display=swap">
<style>
:root{
  --teal:#13aca2;
  --teal-dark:#0f9b92;
  --tint:#c6e5e1;
  --ink:#1c1c1c;
  --rule:#555;
  --paper:#ffffff;
}
*{box-sizing:border-box;margin:0;padding:0}
html,body{width:1200px;height:513px;overflow:hidden;background:var(--paper)}
body{position:relative;font-family:"Lato",sans-serif;color:var(--ink)}

.card{position:absolute;top:0;width:367px;height:513px;background:var(--paper)}
.card--front{left:0}
.card--back{left:834px;width:366px}

.card-header{height:50px;background:var(--teal);color:#fff;text-align:center;display:flex;flex-direction:column;justify-content:center}
.card--front .card-header h1{font-weight:700;font-size:17.5px;line-height:18px}
.card--back .card-header h1{font-weight:700;font-size:18.5px;line-height:20px}
.card-header .hint{font-weight:300;font-size:12px}

.field{position:absolute;font-size:10px;display:flex;align-items:flex-end}
.field .line{flex:1;border-bottom:0.6px solid var(--rule);margin-left:2px;height:8px}

.rate-band{position:absolute;left:0;top:100px;width:367px;height:30px;background:var(--tint);padding:4px 10px;font-size:8.4px;line-height:11px}

.section-head{position:absolute;height:40px;background:var(--teal);color:#fff;display:flex;align-items:center}
.section-head .icon{width:35px;height:35px;border-radius:50%;background:radial-gradient(circle,#f3d9e4 0%,#e9f4f6 60%);border:2px solid #fff;margin:0 6px 0 11px;flex:none}
.section-head h2{font-weight:400;font-size:12.6px;line-height:14.5px}

.task-list{position:absolute;list-style:none;width:170px}
.task-list li{height:20.4px;display:flex;align-items:center;font-family:"Roboto Condensed",sans-serif;font-size:6.1px;letter-spacing:-0.05px;white-space:nowrap}
.task-list--tight li{height:16.3px}
.task-list .label{width:104px;flex:none;overflow:hidden}
.task-list--right .label{width:101px}
.task-list .score{width:11px;height:11px;border:0.8px solid #333;border-radius:50%;flex:none;margin-right:3px}
.task-list .note{flex:1;border-bottom:0.6px solid var(--rule);height:4px}

.card-footer{position:absolute;left:0;bottom:0;width:367px;height:25px;background:var(--teal);color:#fff;font-size:7.6px;text-align:center;line-height:25px}

.stage-label{position:absolute;left:536px;top:31px;font-family:"Poppins",sans-serif;font-weight:600;font-size:9.6px;letter-spacing:.3px}

.status-list{position:absolute;left:9px;top:57px;list-style:none}
.status-list li{display:flex;align-items:center;height:17px;font-size:9.3px;white-space:nowrap}
.status-list .pick{width:12px;height:12px;border:0.8px solid #333;border-radius:50%;margin-right:7px}
.status-list strong{font-size:13.4px;font-weight:700;margin-right:3px}

.reflection-title{position:absolute;left:11px;top:116px;color:var(--teal);font-weight:700;font-size:13.5px}
.question{position:absolute;left:11px;width:345px;font-size:10px;display:flex;align-items:flex-end}
.question .line{flex:1;border-bottom:0.6px solid var(--rule);height:8px;margin-left:1px}

.tint-panel{position:absolute;left:0;width:366px;background:var(--tint);padding:0 9px}
.tint-panel h3{color:var(--teal);font-weight:700;font-size:16.5px}
.tint-panel h3 small{color:var(--ink);font-size:8.6px;font-weight:400}
.tint-row{display:flex;align-items:flex-end;font-size:10.4px;white-space:nowrap}
.tint-row b{color:var(--teal);font-weight:700;font-size:14px;margin-right:3px}
.tint-row .line{flex:1;border-bottom:0.6px solid var(--rule);height:8px;margin-left:1px}

.sign{position:absolute;top:461px;width:170px;border-top:0.6px solid var(--rule);font-size:10px}
.sign p{margin-top:5px}
.sign .date{display:flex;align-items:flex-end;margin-top:13px}
.sign .date .line{flex:1;border-bottom:0.6px solid var(--rule);height:8px}
</style>
</head>
<body>

<section class="card card--front">
  <header class="card-header"><h1>Receptionist<br>Daily Excellence Scorecard</h1></header>
  <div class="field" style="left:9px;top:61px;width:348px">Name:<span class="line"></span></div>
  <div class="field" style="left:9px;top:82px;width:170px">Date:<span class="line"></span></div>
  <div class="field" style="left:179px;top:82px;width:179px">Location:<span class="line"></span></div>
  <div class="rate-band">Please rate yourself for each task:<br>1 = Needs Improvement, 3 = Meets Expectations, 5 = Excellent)</div>

  <div class="section-head" style="left:0;top:136px;width:146px"><span class="icon" role="img" aria-label="Receptionist with headset illustration"></span><h2>Call Handling &amp;<br>First Call Intake</h2></div>
  <div class="section-head" style="left:185px;top:136px;width:182px"><span class="icon" role="img" aria-label="Clothing and flowers illustration"></span><h2>Clothing &amp; Flowers</h2></div>
  <ul class="task-list" style="left:9px;top:178px">
    <li><span class="label">Answered 90%+ calls within 3 rings</span><span class="score"></span><span class="note"></span></li>
    <li><span class="label">Maintained empathy and professionalism</span><span class="score"></span><span class="note"></span></li>
    <li><span class="label">Accurately completed all First Call fields</span><span class="score"></span><span class="note"></span></li>
    <li><span class="label">Worked within Receptionist role</span><span class="score"></span><span class="note"></span></li>
  </ul>
  <ul class="task-list task-list--right task-list--tight" style="left:191px;top:179px;width:166px">
    <li><span class="label">Clothing sheet completed</span><span class="score"></span><span class="note"></span></li>
    <li><span class="label">Family contact noted on sheet</span><span class="score"></span><span class="note"></span></li>
    <li><span class="label">Floral deliveries logged</span><span class="score"></span><span class="note"></span></li>
    <li><span class="label">Concerns communicated to Care Center</span><span class="score"></span><span class="note"></span></li>
    <li><span class="label">Flower placement verified</span><span class="score"></span><span class="note"></span></li>
  </ul>

  <div class="section-head" style="left:0;top:262px;width:179px"><span class="icon" role="img" aria-label="Phone and clock illustration"></span><h2>Call Management<br>&nbsp;During Busy Times</h2></div>
  <div class="section-head" style="left:185px;top:262px;width:182px"><span class="icon" role="img" aria-label="Certificate document illustration"></span><h2>Death Certificates</h2></div>
  <ul class="task-list" style="left:9px;top:303px">
    <li><span class="label">Prioritized urgent vs. non-urgent calls</span><span class="score"></span><span class="note"></span></li>
    <li><span class="label">Hold times under 1 minute</span><span class="score"></span><span class="note"></span></li>
    <li><span class="label">Logged all calls</span><span class="score"></span><span class="note"></span></li>
    <li><span class="label">Requested help if overwhelmed</span><span class="score"></span><span class="note"></span></li>
  </ul>
  <ul class="task-list task-list--right" style="left:191px;top:303px;width:166px">
    <li><span class="label">Verified recipient ID &amp; relationship</span><span class="score"></span><span class="note"></span></li>
    <li><span class="label">Confirmed correct documents enclosed</span><span class="score"></span><span class="note"></span></li>
    <li><span class="label">Recipient signed the DC logbook</span><span class="score"></span><span class="note"></span></li>
    <li><span class="label">Suggested proofreading before leaving</span><span class="score"></span><span class="note"></span></li>
  </ul>

  <div class="section-head" style="left:0;top:388px;width:171px"><span class="icon" role="img" aria-label="Calendar and target illustration"></span><h2>Scheduling Accuracy</h2></div>
  <div class="section-head" style="left:185px;top:388px;width:182px"><span class="icon" role="img" aria-label="Route arrows and map pin illustration"></span><h2>Routing &amp; Messages</h2></div>
  <ul class="task-list" style="left:9px;top:429px">
    <li><span class="label">Updated scheduling board</span><span class="score"></span><span class="note"></span></li>
    <li><span class="label">Cross-checked with Red Book</span><span class="score"></span><span class="note"></span></li>
    <li><span class="label">Entered manifold info promptly</span><span class="score"></span><span class="note"></span></li>
  </ul>
  <ul class="task-list task-list--right" style="left:191px;top:429px;width:166px">
    <li><span class="label">Calls routed appropriately</span><span class="score"></span><span class="note"></span></li>
    <li><span class="label">Messages included all required info</span><span class="score"></span><span class="note"></span></li>
    <li><span class="label">Delivered 95%+ messages in 30 min</span><span class="score"></span><span class="note"></span></li>
  </ul>

  <footer class="card-footer">Self-Rating (1-5)</footer>
</section>

<p class="stage-label">5′ X 7′ Scorecard (Front &amp; Back)</p>

<section class="card card--back">
  <header class="card-header"><h1>Daily Status Summary</h1><span class="hint">(Circle One)</span></header>
  <ul class="status-list">
    <li><span class="pick"></span><strong>Excellent</strong>&nbsp;– All key duties completed, proactive, calm under pressure</li>
    <li><span class="pick"></span><strong>Satisfactory</strong>&nbsp;– Most duties completed, minor follow-up needed</li>
    <li><span class="pick"></span><strong>Needs Support</strong>&nbsp;– Missed urgent duties, accuracy or stress issues</li>
  </ul>
  <h2 class="reflection-title">Daily Reflection</h2>
  <div class="question" style="top:145px">What went well today?<span class="line"></span></div>
  <div class="question" style="top:178px">Any issues or barriers to note?<span class="line"></span></div>
  <div class="question" style="top:210px">Support needed from supervisor?<span class="line"></span></div>

  <div class="tint-panel" style="top:232px;height:94px;padding-top:4px">
    <h3>Stars &amp; Flags <small>(Supervisor Use Only)</small></h3>
    <div class="tint-row" style="margin-top:8px"><b>Stars</b>(Excellence or above-and-beyond moments):<span class="line"></span></div>
    <div class="tint-row" style="margin-top:11px"><b>Flags</b>(Concerns needing follow-up/coaching):<span class="line"></span></div>
  </div>
  <div class="tint-panel" style="top:335px;height:80px;padding-top:6px">
    <h3>Manager's Overall Rating</h3>
    <div class="tint-row" style="font-size:9.2px;margin-top:3px">Manager: (Please rate overall performance on a 1-5 scale)</div>
    <div class="tint-row" style="font-size:9.2px;margin-top:14px">Manager Overall Rating (1-5):<span class="line"></span></div>
  </div>

  <div class="sign" style="left:10px"><p>Receptionist Signature:</p><div class="date">Date:<span class="line"></span></div></div>
  <div class="sign" style="left:186px"><p>Supervisor Signature:</p><div class="date">Date:<span class="line"></span></div></div>
</section>

</body>
</html>
```